Corrow Family Farm fresh honey jar label

I need a label for jars of honey harvested at our farm. These are for gifts and personal use. We are looking to incorporate our farm brand into the label. We would like the design to take the existing brand and add some element like bees, honey, flowers, or hives to indicate the contents. We want the design to feel homemade and authentic without feeling cheap or hoaky

Requirements
Must have
• The label must be made to fit a 1" x2" rectangular label. The label must include the attached family brand. The label must include the text "Corrow Family Farms" "Pinebrook, USA" "Farm Fresh Honey". The label will be printed on off-white paper
Nice to have
• It would be nice to have illustrations of bees or flowers around the logo or hives or honeycombs. The label should have a vintage feel
Should not have
• The label should not feel overly cartoonish or hoaky

```html
<!DOCTYPE html>
<html lang="en">
<head>
<meta charset="utf-8">
<title>Corrow Family Farms – Farm Fresh Honey Label</title>
<link rel="stylesheet" href="https://fonts.googleapis.com/css2?family=Montserrat:wght@600&family=Fraunces:opsz,wght@72,400&family=Lora:wght@400&display=swap">
<style>
  :root {
    --backdrop: #e4e4e6;
    --label-paper: #efe2cb;
    --ink-brown: #4a2a1f;
    --art-tone-light: #e6d6bc;
    --art-tone-dark: #cdb79a;
  }
  * { box-sizing: border-box; margin: 0; padding: 0; }
  html, body {
    width: 1200px;
    height: 1200px;
    overflow: hidden;
    background: var(--backdrop);
  }
  .canvas {
    position: relative;
    width: 1200px;
    height: 1200px;
  }
  .honey-label {
    position: absolute;
    left: 320px;
    top: 100px;
    width: 560px;
    height: 1000px;
    background: var(--label-paper);
    border-radius: 22px;
    color: var(--ink-brown);
    text-align: center;
  }
  .label-frame {
    position: absolute;
    inset: 0;
    width: 560px;
    height: 1000px;
  }
  .brand-block {
    position: absolute;
    left: 0;
    right: 0;
    top: 72px;
    display: flex;
    flex-direction: column;
    align-items: center;
    gap: 48px;
  }
  .brand-square {
    width: 150px;
    height: 150px;
    background: var(--ink-brown);
  }
  .farm-name {
    font-family: "Montserrat", sans-serif;
    font-weight: 600;
    font-size: 33px;
    line-height: 1;
    letter-spacing: 0.5px;
    white-space: nowrap;
  }
  .honey-artwork {
    position: absolute;
    left: 70px;
    top: 395px;
    width: 420px;
    height: 285px;
    border-radius: 10px;
    background: radial-gradient(ellipse at center, var(--art-tone-dark) 0%, var(--art-tone-light) 75%);
  }
  .product-name {
    position: absolute;
    left: 0;
    right: 0;
    top: 692px;
    font-family: "Fraunces", serif;
    font-weight: 400;
    font-size: 58px;
    line-height: 1.2;
  }
  .origin {
    position: absolute;
    left: 0;
    right: 0;
    top: 892px;
    font-family: "Lora", serif;
    font-size: 32px;
    line-height: 1;
    letter-spacing: 0.5px;
  }
</style>
</head>
<body>
<main class="canvas">
  <section class="honey-label">
    <svg class="label-frame" viewBox="0 0 560 1000" aria-hidden="true">
      <path d="M76 34 H490 A30 30 0 0 0 520 64 V936 A30 30 0 0 0 490 966 H76 A30 30 0 0 0 46 936 V64 A30 30 0 0 0 76 34 Z"
            fill="none" stroke="var(--ink-brown)" stroke-width="4"/>
    </svg>

    <div class="brand-block">
      <span class="brand-square" aria-hidden="true"></span>
      <p class="farm-name">CORROW FAMILY FARMS</p>
    </div>

    <div class="honey-artwork" role="img" aria-label="Vintage engraved sketch of a cloth-topped honey jar with two bees flying on either side"></div>

    <h1 class="product-name">Farm Fresh<br>Honey</h1>

    <p class="origin">PINEBROOK, USA</p>
  </section>
</main>
</body>
</html>
```